Harborvale LLC
256-738-1054
438 Corwin T. Maddox Blvd.
Marrowton, AL 35088
harborvalellc97@quillmarsh.com

Heavy& Light Duty Diesel Truck, Trailer, and Equipment Repair
Certified RKT Master Tech & trained techs

Services:
alignments, brakes, suspension, A/C, engine overhauls, DOT inspections, fleet maintenance, computer diagnosis for gas & diesel, warranty work, performance parts for all diesel pickups, Welding & fabrication

Colors, text for Company, phone number, email address in bright red, all other text black.
background color of postcard light grey, black border around pictures.

Industry/Entity Type

Computer

Colors
ec2027

```html
<!DOCTYPE html>
<html lang="en">
<head>
<meta charset="utf-8">
<title>Harborvale LLC Postcard</title>
<link href="https://fonts.googleapis.com/css2?family=Luckiest+Guy&display=swap" rel="stylesheet">
<style>
  :root {
    --red: #ec2027;
    --ink: #111111;
    --panel: #a9a9a9;
    --paper: #ffffff;
    --stage: #2e2e2e;
    --stamp: #9a9a9a;
  }
  * { box-sizing: border-box; margin: 0; padding: 0; }
  html, body { width: 1200px; height: 900px; overflow: hidden; }
  body {
    background: var(--stage);
    font-family: "Luckiest Guy", "Arial Black", sans-serif;
    color: var(--ink);
    display: flex;
    align-items: center;
    justify-content: center;
    gap: 36px;
  }
  .postcard {
    position: relative;
    width: 560px;
    height: 374px;
    background: var(--paper);
    box-shadow: 0 12px 30px rgba(0,0,0,.45);
    overflow: hidden;
  }
  .postcard svg.card-art { position: absolute; inset: 0; width: 100%; height: 100%; }
  .postcard .text {
    position: absolute;
    line-height: 1.15;
    letter-spacing: .3px;
    text-transform: uppercase;
    font-weight: 400;
  }

  /* front */
  .company-name {
    right: 22px; top: 188px;
    font-size: 28px; color: var(--red);
    white-space: nowrap;
  }
  .tagline {
    right: 16px; top: 232px; width: 400px;
    font-size: 12px; text-align: center;
    white-space: nowrap;
  }
  .services-label { left: 26px; top: 300px; font-size: 14px; }
  .services-list { left: 26px; top: 324px; width: 510px; font-size: 9px; line-height: 1.3; }

  /* back */
  .phone { left: 92px; top: 160px; font-size: 21px; color: var(--red); white-space: nowrap; }
  .address { left: 66px; top: 200px; font-size: 10px; color: var(--red); line-height: 1.25; white-space: nowrap; }
  .email { left: 56px; top: 232px; font-size: 10px; color: var(--red); white-space: nowrap; }
</style>
</head>
<body>

<section class="postcard postcard-front" aria-label="Postcard front">
  <svg class="card-art" viewBox="0 0 560 374">
    <defs>
      <linearGradient id="shopPhoto" x1="0" y1="0" x2="0" y2="1">
        <stop offset="0" stop-color="#5f8fd6"/>
        <stop offset=".45" stop-color="#d9d3c6"/>
        <stop offset="1" stop-color="#a99a80"/>
      </linearGradient>
    </defs>
    <rect x="0" y="0" width="560" height="374" fill="var(--ink)"/>
    <polygon class="shop-photo" role="img" aria-label="Photo of the repair shop building with diesel pickups and a service truck parked in front"
      points="10,10 550,10 550,146 128,172 10,156" fill="url(#shopPhoto)"/>
    <polygon class="grey-panel" points="10,170 128,188 550,160 550,364 10,364" fill="var(--panel)"/>
    <circle class="accent-dot" cx="14" cy="196" r="44" fill="var(--red)" stroke="var(--ink)" stroke-width="7"/>
    <line x1="180" y1="225" x2="550" y2="225" stroke="var(--ink)" stroke-width="2.5"/>
    <line x1="26" y1="318" x2="175" y2="318" stroke="var(--ink)" stroke-width="2"/>
  </svg>
  <h1 class="text company-name">Harborvale LLC</h1>
  <p class="text tagline">Heavy&amp; Light Duty Diesel Truck, Trailer,<br>and Equipment Repair<br>Certified RKT Master Tech &amp; Trained Techs</p>
  <h2 class="text services-label">Services:</h2>
  <p class="text services-list">Alignments, brakes, suspension, A/C, engine overhauls, DOT inspections, fleet maintenance, computer diagnosis for gas &amp; diesel, warranty work, performance parts for all diesel pickups, welding &amp; fabrication</p>
</section>

<section class="postcard postcard-back" aria-label="Postcard back">
  <svg class="card-art" viewBox="0 0 560 374">
    <defs>
      <linearGradient id="scanPhoto" x1="0" y1="0" x2="1" y2="1">
        <stop offset="0" stop-color="#3c4a5e"/>
        <stop offset=".5" stop-color="#262b33"/>
        <stop offset="1" stop-color="#4b6d9a"/>
      </linearGradient>
    </defs>
    <polygon class="contact-frame" points="0,0 318,0 262,374 0,374" fill="var(--ink)"/>
    <polygon class="scan-photo" role="img" aria-label="Photo of a technician holding a diagnostic scan tablet inside a truck cab"
      points="10,10 306,10 290,116 10,148" fill="url(#scanPhoto)"/>
    <polygon class="grey-panel" points="10,160 288,128 252,364 10,364" fill="var(--panel)"/>
    <line x1="66" y1="190" x2="270" y2="190" stroke="var(--ink)" stroke-width="2.5"/>
    <circle class="accent-dot" cx="226" cy="316" r="56" fill="var(--red)" stroke="var(--ink)" stroke-width="7"/>
    <rect class="stamp-box" x="486" y="30" width="48" height="54" fill="none" stroke="var(--stamp)" stroke-width="2"/>
    <g class="address-lines" stroke="var(--ink)" stroke-width="1.6">
      <line x1="335" y1="196" x2="535" y2="196"/>
      <line x1="335" y1="222" x2="535" y2="222"/>
      <line x1="335" y1="248" x2="535" y2="248"/>
      <line x1="335" y1="274" x2="535" y2="274"/>
    </g>
  </svg>
  <p class="text phone">256-738-1054</p>
  <p class="text address">438 Corwin T. Maddox Blvd.<br>Marrowton, AL 35088</p>
  <p class="text email">harborvalellc97@quillmarsh.com</p>
</section>

</body>
</html>
```